Need a cool business card design that matches our logo

Hi there,

I need a business card design that matches our logo, I would prefer round corners... It has to be modern and cool, be creative! Our logo consists of two elements, the writing and a Icon which can be placed in different positions. Have fun!

```html
<!DOCTYPE html>
<html lang="en">
<head>
<meta charset="utf-8">
<title>teamuptoday – business cards</title>
<link rel="stylesheet" href="https://fonts.googleapis.com/css2?family=Open+Sans:wght@400;600;800&display=swap">
<style>
  :root {
    --backdrop: #3a3a3a;
    --card-black: #1f1f1f;
    --card-black-light: #2c2c2c;
    --card-white: #ffffff;
    --brand-orange: #f26a22;
    --brand-orange-light: #f79a3c;
    --text-light: #e8e8e8;
    --text-muted: #a9a9a9;
  }
  * { margin: 0; padding: 0; box-sizing: border-box; }
  html, body {
    width: 1200px; height: 799px; overflow: hidden;
    background: var(--backdrop);
    font-family: "Open Sans", Arial, sans-serif;
  }
  .sheet {
    position: relative; width: 1200px; height: 799px;
    display: flex; align-items: center; justify-content: center; gap: 60px;
  }
  .card {
    position: relative; width: 500px; height: 290px;
    border-radius: 16px; overflow: hidden;
    background: var(--card-black);
  }
  .card__shape { position: absolute; inset: 0; }
  .front__brand {
    position: absolute; left: 20px; top: 132px;
    display: flex; align-items: center; gap: 6px;
    font-weight: 800; font-size: 19px; line-height: 26px;
    color: var(--brand-orange); white-space: nowrap;
  }
  .brand-dot {
    width: 12px; height: 12px; border-radius: 50%; background: var(--brand-orange);
  }
  .contact {
    position: absolute; right: 30px; top: 40px;
    text-align: right; color: var(--text-light);
  }
  .contact__name { font-weight: 600; font-size: 14px; }
  .contact__role { font-size: 10px; color: var(--text-muted); margin-bottom: 18px; }
  .contact__address { font-size: 10.5px; line-height: 1.6; margin-bottom: 16px; }
  .contact__line {
    display: flex; justify-content: flex-end; align-items: center; gap: 8px;
    font-size: 10.5px; line-height: 1.65;
  }
  .contact__line svg { width: 10px; height: 10px; fill: var(--text-light); }
  .back {
    background: linear-gradient(160deg, var(--card-black-light), var(--card-black) 60%);
    display: flex; flex-direction: column; align-items: center; justify-content: center;
  }
  .back__brand {
    font-weight: 800; font-size: 46px; color: var(--brand-orange);
    letter-spacing: -1px; margin-top: 10px;
  }
  .back__web { margin-top: 34px; font-size: 11px; letter-spacing: 1.5px; color: var(--text-light); }
</style>
</head>
<body>
<main class="sheet">
  <section class="card front">
    <svg class="card__shape" viewBox="0 0 500 290" aria-hidden="true">
      <path d="M0 0 H252 Q172 145 252 290 H0 Z" fill="var(--brand-orange)"/>
      <path d="M0 0 H240 Q160 145 240 290 H0 Z" fill="var(--brand-orange-light)"/>
      <path d="M0 0 H232 Q152 145 232 290 H0 Z" fill="var(--card-white)"/>
    </svg>
    <div class="front__brand"><span class="brand-dot"></span>teamuptoday</div>
    <div class="contact">
      <p class="contact__name">Mark Halden</p>
      <p class="contact__role">Director</p>
      <p class="contact__address">1420 Willow Creek Lane<br>Suite 210<br>Dayton, Ohio 4521</p>
      <p class="contact__line">072 418 3360
        <svg viewBox="0 0 10 10"><path d="M1 3 Q1 1 3 1 H7 Q9 1 9 3 L7 4 L6 3 H4 L3 4 Z M2 5 H8 V9 H2 Z"/></svg></p>
      <p class="contact__line">072 418 3361
        <svg viewBox="0 0 10 10"><path d="M3 1 H7 V4 H3 Z M1 4 H9 V9 H1 Z"/></svg></p>
      <p class="contact__line">mark@teamuptoday.com
        <svg viewBox="0 0 10 10"><path d="M1 2 H9 V8 H1 Z M1.6 2.6 L5 5.4 L8.4 2.6 Z" fill-rule="evenodd"/></svg></p>
      <p class="contact__line">www.teamuptoday.com
        <svg viewBox="0 0 10 10"><circle cx="5" cy="5" r="4" fill="none" stroke="#e8e8e8" stroke-width="1.2"/><circle cx="5" cy="5" r="1.5"/></svg></p>
    </div>
  </section>

  <section class="card back">
    <p class="back__brand">teamuptoday</p>
    <p class="back__web">www.teamuptoday.com</p>
  </section>
</main>
</body>
</html>
```